Postcard Design

Name of the Company is : Tidewell Harbor Sport Fishing Charters Block Island RI
Name of the boat : Kelp Ora Vim
local Captain Darnell Okafor
pricing and booking : 738-615-2904
We specialize in:

Shark & Tuna Trips
Full or half day Inshore Bass & Bluefish
Half day bottom fishing for Fluke, Sea Bass & Scup
Inshore night fishing trips
Custom Combination Charters also available
Our crew provides:
A professional and accommodating experience
A very child friendly environment
A range of technique options for every style of trip
An immense knowledge of the waters.
Our Vessel:
Meets all NMRB safety requirement
Twin 250 Hp Voskard Turbo Diesels
All updated electronics
On the comfort side : we have a restroom, and a galley area with a table so you can enjoy your lunch.

Payments : We except; Cash , Check , Qr, Lb, Pz and Ot

I have attached the logo I would like to use . If possible I would like to use the banners on the logo with Company Name & number.

```html
<!DOCTYPE html>
<html lang="en">
<head>
<meta charset="utf-8">
<title>Tidewell Harbor Sport Fishing Charters – Postcard</title>
<link href="https://fonts.googleapis.com/css2?family=Open+Sans:wght@700&family=Roboto+Condensed:wght@400&display=swap" rel="stylesheet">
<style>
  :root {
    --navy: #1b3a6b;
    --deep-blue: #1656a8;
    --mid-blue: #1f79c9;
    --light-blue: #2f9fe0;
    --foam: #8fd0f2;
    --sky-white: #ffffff;
    --label-yellow: #f4e83c;
    --text-white: #ffffff;
  }
  html, body {
    margin: 0;
    padding: 0;
    width: 1200px;
    height: 933px;
    overflow: hidden;
    background: var(--sky-white);
  }
  .postcard {
    position: relative;
    width: 1200px;
    height: 933px;
    overflow: hidden;
    background: var(--sky-white);
  }
  .sea {
    position: absolute;
    inset: 0;
    width: 1200px;
    height: 933px;
  }
  .brand {
    position: absolute;
    left: 80px;
    top: 70px;
    width: 480px;
    text-align: center;
    font-family: "Open Sans", Arial, sans-serif;
    font-weight: 700;
    color: var(--navy);
  }
  .brand-name {
    margin: 0;
    font-size: 34px;
    line-height: 1.2;
  }
  .brand-mark {
    display: block;
    width: 26px;
    height: 26px;
    margin: 0 auto 14px;
    border-radius: 50%;
    background: var(--navy);
  }
  .brand-phone {
    margin: 18px 0 0;
    font-size: 34px;
    color: var(--navy);
  }
  .boat-details {
    position: absolute;
    left: 60px;
    top: 436px;
    width: 516px;
    text-align: center;
  }
  .detail-label {
    margin: 0;
    font-family: "Roboto Condensed", "Arial Narrow", sans-serif;
    font-size: 29px;
    line-height: 34px;
    color: var(--label-yellow);
  }
  .detail-value {
    margin: 0 0 26px;
    font-family: "Open Sans", Arial, sans-serif;
    font-weight: 700;
    font-size: 52px;
    line-height: 62px;
    color: var(--text-white);
  }
  .detail-value.phone { font-size: 56px; }
  .offer {
    position: absolute;
    left: 612px;
    top: 250px;
    width: 560px;
    font-family: "Roboto Condensed", "Arial Narrow", sans-serif;
    font-size: 31px;
    line-height: 39px;
    color: var(--text-white);
  }
  .offer-heading {
    margin: 0 0 18px 31px;
    font-size: 31px;
    font-weight: 400;
  }
  .offer-list {
    list-style: none;
    margin: 0 0 32px;
    padding: 0;
  }
  .offer-list li {
    position: relative;
    padding-left: 31px;
  }
  .offer-list svg {
    position: absolute;
    left: 2px;
    top: 12px;
    width: 20px;
    height: 16px;
  }
</style>
</head>
<body>
<main class="postcard">
  <svg class="sea" viewBox="0 0 1200 933" aria-hidden="true">
    <defs>
      <linearGradient id="sea-body" x1="0" y1="0" x2="0" y2="1">
        <stop offset="0" stop-color="var(--deep-blue)"/>
        <stop offset="0.55" stop-color="var(--mid-blue)"/>
        <stop offset="1" stop-color="var(--light-blue)"/>
      </linearGradient>
      <linearGradient id="wave-crest" x1="0" y1="0" x2="1" y2="0">
        <stop offset="0" stop-color="#cfeefb"/>
        <stop offset="1" stop-color="#5fb9ec"/>
      </linearGradient>
    </defs>
    <path d="M0 90 C120 150 220 70 330 150 C420 210 520 190 600 150 C700 95 800 40 900 45 C1000 50 1080 10 1200 30 L1200 933 L0 933 Z" fill="url(#wave-crest)"/>
    <path d="M0 265 C100 250 180 300 300 290 C420 280 480 250 560 215 C660 170 760 120 880 140 C980 155 1060 110 1130 80 C1160 68 1185 75 1200 85 L1200 933 L0 933 Z" fill="url(#sea-body)"/>
  </svg>

  <header class="brand">
    <span class="brand-mark"></span>
    <h1 class="brand-name">Tidewell Harbor Sport Fishing Charters</h1>
    <p class="brand-phone">(738) 615-2904</p>
  </header>

  <section class="boat-details">
    <p class="detail-label">Name of our boat:</p>
    <p class="detail-value">Kelp Ora Vim</p>
    <p class="detail-label">Local Captain</p>
    <p class="detail-value">Darnell Okafor</p>
    <p class="detail-label">Pricing &amp; Booking</p>
    <p class="detail-value phone">(738) 615-2904</p>
  </section>

  <section class="offer">
    <h2 class="offer-heading">We specialize in:</h2>
    <ul class="offer-list">
      <li><svg viewBox="0 0 20 16"><path d="M0 8 L14 2 L11 7 L20 8 L11 9 L14 14 Z" fill="#fff"/></svg>Shark &amp; Tuna Trips</li>
      <li><svg viewBox="0 0 20 16"><path d="M0 8 L14 2 L11 7 L20 8 L11 9 L14 14 Z" fill="#fff"/></svg>Full or half day Inshore Bass &amp; Bluefish</li>
      <li><svg viewBox="0 0 20 16"><path d="M0 8 L14 2 L11 7 L20 8 L11 9 L14 14 Z" fill="#fff"/></svg>Half day bottom fishing for Fluke,<br>Sea Bass &amp; Scup</li>
      <li><svg viewBox="0 0 20 16"><path d="M0 8 L14 2 L11 7 L20 8 L11 9 L14 14 Z" fill="#fff"/></svg>Inshore night fishing trips</li>
      <li><svg viewBox="0 0 20 16"><path d="M0 8 L14 2 L11 7 L20 8 L11 9 L14 14 Z" fill="#fff"/></svg>Custom Combination Charters available</li>
    </ul>
    <h2 class="offer-heading">Our crew provides:</h2>
    <ul class="offer-list">
      <li><svg viewBox="0 0 20 16"><path d="M0 8 L14 2 L11 7 L20 8 L11 9 L14 14 Z" fill="#fff"/></svg>A professional and accommodating<br>experience</li>
      <li><svg viewBox="0 0 20 16"><path d="M0 8 L14 2 L11 7 L20 8 L11 9 L14 14 Z" fill="#fff"/></svg>A very child friendly environment</li>
      <li><svg viewBox="0 0 20 16"><path d="M0 8 L14 2 L11 7 L20 8 L11 9 L14 14 Z" fill="#fff"/></svg>A range of technique options for<br>every style of trip</li>
      <li><svg viewBox="0 0 20 16"><path d="M0 8 L14 2 L11 7 L20 8 L11 9 L14 14 Z" fill="#fff"/></svg>An immense knowledge of the waters</li>
    </ul>
  </section>
</main>
</body>
</html>
```